Interior Design Site

We need a website design for an interior design company which will be quite image heavy. The designs need to be compatible with Dot Net Nuke 5 skins and containers as the PSD file will need to converted to this content management system.

Target Market(s)

General public

Industry/Entity Type

Interior

Number of Pages Required

3 pages

Requirements
Must have
• I have attached some wireframes for layout of each page......they would like a side navigation on left hand side so for Page 2 and 3 can you reduce the text box in width to match the images on page 2, allowing for a side nav to sit on left hand side. Page 3 should have the image placeholder modified in the same way.
The four sections are
1. About
2. Services
3. Projects
4. Life
White background, shadow lines (similar to the www.kestrelwheelsmarlo.com.au) where appropriate, though square edges. Pantone 021 is key corporate colour and good for any action points and Pantone 877 for text. The pink in the brochure (attached for visual reference) is a 12M, 20Y but probably a bit light for web.

Their font is Gill Sans (attached). Prefer to use this for key buttons but understand the need to use system fonts elsewhere.

Logo, both as square and rectangle are attached. Top left above the hero image for this, though I''d say the rectangle will work best.

```html
<!DOCTYPE html>
<html lang="en">
<head>
<meta charset="utf-8">
<title>Kinloch Interiors – Site Pages</title>
<link href="https://fonts.googleapis.com/css2?family=Didact+Gothic&display=swap" rel="stylesheet">
<style>
:root{
  --orange:#f7901e;
  --text:#58585a;
  --muted:#9a9a9a;
  --band:#fde2c9;
  --white:#ffffff;
}
*{margin:0;padding:0;box-sizing:border-box}
html,body{width:1200px;height:3326px;overflow:hidden;background:var(--white)}
body{position:relative;font-family:"Didact Gothic",Arial,sans-serif;color:var(--text)}
a{color:var(--orange);text-decoration:none}
.page{position:absolute;left:0;width:1200px}
.page--home{top:0;height:1341px}
.page--services{top:1341px;height:1032px}
.page--projects{top:2373px;height:953px}
.abs{position:absolute}

.brand{position:absolute;left:24px;font-size:30px;color:var(--text);display:flex;align-items:center;gap:12px}
.brand-mark{width:16px;height:16px;background:var(--orange)}
.main-nav{position:absolute;right:22px;display:flex;align-items:center;gap:4px;font-size:22px}
.main-nav a{padding:5px 13px;border-radius:20px;line-height:27px}
.main-nav a.is-active{background:var(--orange);color:var(--white);font-weight:bold}

.photo{position:absolute}
.hero{left:0;top:120px;width:1200px;height:381px;background:linear-gradient(100deg,#8a4a22 0%,#c9955a 22%,#9d8e7c 45%,#b79a6e 65%,#6e5a48 85%,#5a6f93 100%)}
.tiles{position:absolute;left:127px;top:443px;display:flex;gap:2px}
.tile{width:233px}
.tile-photo{height:127px}
.tile-label{height:46px;background:var(--orange);color:var(--white);font-size:28px;text-align:center;line-height:46px}

.heading{color:var(--orange);font-weight:normal}
.home-copy{font-size:22px;line-height:26px}
.home-copy p{margin-bottom:26px}

.footer{position:absolute;left:0;width:1200px;height:47px;background:var(--orange);color:var(--white);font-size:16.5px;line-height:47px;text-align:center;word-spacing:1px}
.footer span{margin:0 12px}

.section-band{position:absolute;left:0;width:1200px;height:83px;background:var(--band)}
.section-band h1{position:absolute;left:26px;top:20px;font-size:31px;font-weight:normal;color:var(--orange)}
.side-nav{position:absolute;left:26px;width:210px;list-style:none;font-size:17px;line-height:20px}
.side-nav li{margin-bottom:20px}
.side-nav .is-current{color:var(--muted)}
.small-copy{font-size:18px;line-height:20px}
.small-copy p{margin-bottom:26px}
.thumbs{position:absolute;left:792px;display:grid;grid-template-columns:repeat(3,120px);grid-auto-rows:80px;gap:9px 10px}
</style>
</head>
<body>

<section class="page page--home">
  <div class="brand" style="top:40px"><span class="brand-mark"></span>Kinloch Interiors</div>
  <nav class="main-nav" style="top:42px">
    <a class="is-active">Home</a><a>About</a><a>Services</a><a>Projects</a><a>Life</a><a>Contact</a>
  </nav>
  <div class="photo hero" role="img" aria-label="Interior photo of a brick and timber living space with high ceilings"></div>
  <div class="tiles">
    <div class="tile"><div class="tile-photo" style="background:linear-gradient(135deg,#d9c7b2,#f3ece4 60%,#c8b090)" role="img" aria-label="Portrait of the lead designer"></div><div class="tile-label">About</div></div>
    <div class="tile"><div class="tile-photo" style="background:linear-gradient(135deg,#c9a56a,#e8dcc0 50%,#6fa2c4)" role="img" aria-label="Floor plan drawing"></div><div class="tile-label">Services</div></div>
    <div class="tile"><div class="tile-photo" style="background:linear-gradient(135deg,#a8522a,#d48a4c 50%,#e9c9a6)" role="img" aria-label="Timber kitchen interior"></div><div class="tile-label">Projects</div></div>
    <div class="tile"><div class="tile-photo" style="background:linear-gradient(135deg,#b39a76,#e6d9c4 45%,#d8452e)" role="img" aria-label="Close-up of patterned cushion fabric"></div><div class="tile-label">Life</div></div>
  </div>

  <h2 class="abs heading" style="left:57px;top:676px;font-size:29px">Lifestyle and Design Solutions</h2>
  <div class="abs home-copy" style="left:57px;top:735px;width:665px">
    <p>Kinloch Interiors is a modern and innovative company, established to make the creative process, from concept through to completion, seamless for our clientele.</p>
    <p>Lorem ipsum dolor sit amet, consectetur adipiscing elit. Praesent sed libero. Ut <a>malesuada</a>. Cras non leo id enim condimentum placerat. Maecenas eleifend ligula a sem. Praesent ultrices felis pellentesque eros. Morbi vel lectus vel urna eleifend bibendum.</p>
    <p style="margin-top:40px">Integer blandit lorem sed augue. Ut luctus, mi eget tristique lacinia, nulla orci sagittis ante, in commodo ante est a ligula. Duis orci felis, condimentum eu, blandit a, ultricies at, massa.</p>
    <p style="margin-top:40px">Suspendisse ac felis. Nunc a lectus. <a>Suspendisse potenti</a>. Donec cursus lectus ac nisl. Aliquam sodales. Curabitur pellentesque. Suspendisse luctus aliquam est. Mauris a leo. Vestibulum ante ipsum primis in faucibus orci</p>
  </div>
  <div class="abs home-copy" style="left:792px;top:682px;width:355px">
    <p><a>Integer blandit lorem</a> sed augue. Ut luctus, mi eget tristique lacinia, nulla orci sagittis ante, in commodo ante est a ligula. Duis orci felis, condimentum eu, blandit a, ultricies at, massa.</p>
    <p style="margin-top:14px">Aenean in leo in sem rutrum elementum. Donec sed metus nec nunc dignissim condimentum. Aliquam porta orci eu diam. Quisque venenatis nulla id tellus.</p>
    <p style="margin-top:14px">Nam a mi. Sed aliquet faucibus nulla. Cras posuere, felis quis vestibulum vestibulum, arcu velit ullamcorper arcu, in volutpat odio nibh eget augue.</p>
  </div>
  <footer class="footer" style="top:1294px"><span>© Kinloch Interiors Pty Ltd</span><span>ABN 12 345 678 901</span><span>0400 555 018</span><span>PO Box 204 Harbour Point Queensland 4000</span></footer>
</section>

<section class="page page--services">
  <div class="brand" style="top:85px"><span class="brand-mark"></span>Kinloch Interiors</div>
  <nav class="main-nav" style="top:88px">
    <a>Home</a><a>About</a><a class="is-active">Services</a><a>Projects</a><a>Life</a><a>Contact</a>
  </nav>
  <div class="section-band" style="top:166px"><h1>Services</h1></div>
  <ul class="side-nav" style="top:280px">
    <li><a>Renovations &amp;<br>Restorations</a></li>
    <li><a>Custom Designed Homes</a></li>
    <li class="is-current">Interior Design</li>
    <li><a>Landscape and Pool<br>Design</a></li>
    <li><a>Project Coordination</a></li>
    <li><a>Construction<br>Management</a></li>
  </ul>
  <h2 class="abs heading" style="left:265px;top:276px;font-size:29px">Loren Ipsum</h2>
  <div class="abs small-copy" style="left:265px;top:333px;width:500px">
    <p>Lorem ipsum dolor sit amet, consectetur adipiscing elit. Praesent sed libero. Ut <a>malesuada</a>. Cras non leo id enim condimentum placerat. Maecenas eleifend ligula a sem. Praesent ultrices felis pellentesque eros. Morbi vel lectus vel urna eleifend bibendum.</p>
    <p>Integer blandit lorem sed augue. Ut luctus, mi eget <a>tristique lacinia</a>, nulla orci sagittis ante, in commodo ante est a ligula. Duis orci felis, condimentum eu, <a>blandit</a> a, ultricies at, massa.</p>
    <p style="margin-top:32px">In cursus commodo lorem. Fusce ipsum leo, tempor eu, euismod a, elementum at, massa. Donec eros. Vivamus consequat pulvinar odio. Morbi non nisl. Aliquam quis felis. In massa. Vivamus dictum massa sit amet felis. Donec lectus. Morbi tortor. Aenean quis velit id turpis commodo laoreet. Aliquam dignissim.</p>
    <p style="margin-top:32px"><a>Suspendisse</a> ac felis. Nunc a lectus. Suspendisse potenti. Donec cursus lectus ac nisl. Aliquam sodales. Curabitur pellentesque. Suspendisse luctus aliquam est. Mauris a leo. Vestibulum ante ipsum primis in faucibus orci luctus et ultrices posuere cubilia Curae;</p>
    <p style="margin-top:32px">Sed mollis orci sit amet turpis. In mollis augue quis lectus. In mattis. Pellentesque lacinia cursus nulla.</p>
  </div>
  <div class="photo" style="left:792px;top:281px;width:380px;height:252px;background:linear-gradient(160deg,#a77c54,#d9cfc2 45%,#eceae6 70%,#6f6a68)" role="img" aria-label="Living room with white sofa and glass coffee table"></div>
  <div class="thumbs" style="top:542px">
    <div style="background:linear-gradient(135deg,#e9d6bf,#b46a2e)" role="img" aria-label="Timber cabinetry detail"></div>
    <div style="background:linear-gradient(135deg,#8b8f95,#f0eee9)" role="img" aria-label="Bedroom with white linen"></div>
    <div style="background:linear-gradient(135deg,#5b4a2d,#dcd2b8)" role="img" aria-label="Table styling with flowers"></div>
    <div style="background:linear-gradient(135deg,#6f8fb2,#eef2f6)" role="img" aria-label="Coastal view from terrace"></div>
    <div style="background:linear-gradient(135deg,#b0521e,#e3a35a)" role="img" aria-label="Warm timber wall panelling"></div>
    <div style="background:linear-gradient(135deg,#4d3f3a,#c8c1bd)" role="img" aria-label="Dark tiled bathroom"></div>
  </div>
  <div class="abs home-copy" style="left:792px;top:730px;width:365px">
    <p><a>Integer blandit lorem</a> sed augue. Ut luctus, mi eget tristique lacinia, nulla orci sagittis ante, in commodo ante est a ligula. Duis orci felis, condimentum eu, blandit a, ultricies at, massa.</p>
  </div>
  <footer class="footer" style="top:985px"><span>© Kinloch Interiors Pty Ltd</span><span>ABN 12 345 678 901</span><span>0400 555 018</span><span>PO Box 204 Harbour Point Queensland 4000</span></footer>
</section>

<section class="page page--projects">
  <div class="brand" style="top:105px"><span class="brand-mark"></span>Kinloch Interiors</div>
  <nav class="main-nav" style="top:107px">
    <a>Home</a><a>About</a><a>Services</a><a class="is-active">Projects</a><a>Life</a><a>Contact</a>
  </nav>
  <div class="section-band" style="top:186px"><h1>Section Header</h1></div>
  <ul class="side-nav" style="top:300px">
    <li><a>Navigation title One</a></li>
    <li><a>Navigation title Two</a></li>
    <li class="is-current">Current page</li>
    <li><a>Navigation title Three</a></li>
    <li><a>Navigation title Four</a></li>
    <li><a>Navigation title Five</a></li>
  </ul>
  <div class="photo" style="left:265px;top:301px;width:505px;height:479px;background:linear-gradient(165deg,#8d5a34,#c9b49a 35%,#e8e6e2 65%,#7a716a)" role="img" aria-label="Open living room with white sofa, coffee table and brick wall"></div>
  <div class="abs small-copy" style="left:792px;top:297px;width:360px">
    <p style="margin-bottom:20px">Mi eget tristique lacinia, nulla orci sagittis ante, in commodo ante est a ligula. Duis orci felis, condimentum eu, blandit a, ultricies at, massa.</p>
    <p style="margin-bottom:20px">In cursus commodo lorem. Fusce ipsum leo, tempor eu, euismod a, elementum at, massa. Donec eros. Vivamus consequat pulvinar odio. Morbi non nisl. Aliquam quis felis. In massa.</p>
    <p>Vivamus dictum massa sit amet felis. Donec lectus. Morbi tortor. Aenean quis velit id turpis commodo laoreet.</p>
  </div>
  <div class="photo" style="left:792px;top:611px;width:385px;height:172px;background:linear-gradient(170deg,#3e3530,#8d8580 40%,#f2efe9 70%,#d9d2c6)" role="img" aria-label="Bedroom with dark headboard and white bedding"></div>
  <footer class="footer" style="top:873px"><span>© Kinloch Interiors Pty Ltd</span><span>ABN 12 345 678 901</span><span>0400 555 018</span><span>PO Box 204 Harbour Point Queensland 4000</span></footer>
</section>

</body>
</html>
```